Business Cards that are elegant and wow

I want to create and print business cards that represent my brand and stand out from the rest. We want to ensure they stay in our branding and the integrity is not lost. I am happy to look at different shapes like square etc.

It will be printed on very thick cards and will be stylish .

I want to create and print business cards that represent my brand and stand out from the rest. We want to ensure they stay in ur branding and the integrity is not lost. I am happy to look at different shapes like square etc.

Target Market(s)

real estate professionals

Industry/Entity Type

Real Estate

Contact Information for Business Card

Maren Holt
hello@brightfernrealty.com.au
brightfernrealty.com.au
0487 316 252 (SMS)

Colors

Designer to choose colors to be used in the design.

Requirements
Must have
• My logo
• email
• website
• Name
Nice to have
• I like the idea of printing with foil or spot gloss. You want it to stand out in a sea.
Should not have
• I would like you to stay in my colour themes. Don't change the colour of my logo

```html
<!DOCTYPE html>
<html lang="en">
<head>
<meta charset="utf-8">
<title>Bright Fern Realty – Business Card</title>
<link href="https://fonts.googleapis.com/css2?family=Oswald:wght@300;500&family=Playfair+Display:wght@700&display=swap" rel="stylesheet">
<style>
  :root {
    --backdrop: #e9e6e1;
    --card-white: #ffffff;
    --card-black: #111111;
    --card-black-edge: #262626;
    --brand-pink: #e8197d;
    --brand-cyan: #1fb3ec;
    --ink: #3b3b3b;
    --emboss: #3a3a3a;
  }
  * { box-sizing: border-box; margin: 0; padding: 0; }
  html, body {
    width: 1200px; height: 1200px; overflow: hidden;
    background: var(--backdrop);
  }
  .sheet {
    position: relative; width: 1200px; height: 1200px;
  }
  .card {
    position: absolute; left: 160px;
    width: 880px; height: 538px;
    border-radius: 4px;
    box-shadow: 0 10px 30px rgba(0,0,0,0.18);
    overflow: hidden;
  }
  /* Front */
  .card--front { top: 40px; background: var(--card-white); }
  .brand {
    position: absolute; left: 60px; top: 64px;
    display: flex; align-items: center; gap: 18px;
  }
  .brand__dot {
    width: 64px; height: 64px; border-radius: 50%;
    border: 6px solid var(--brand-pink);
  }
  .brand__name {
    font-family: "Oswald", sans-serif; font-weight: 500;
    font-size: 50px; letter-spacing: 3px; text-transform: uppercase;
    color: var(--brand-cyan); line-height: 1;
  }
  .holder {
    position: absolute; left: 390px; top: 252px;
    font-family: "Playfair Display", serif; font-weight: 700;
    font-size: 38px; color: var(--brand-pink);
    text-transform: uppercase; letter-spacing: 1px;
  }
  .contacts {
    position: absolute; left: 340px; top: 318px;
    list-style: none;
    font-family: "Oswald", sans-serif; font-weight: 300;
    font-size: 27px; color: var(--ink);
  }
  .contacts li {
    display: flex; align-items: center; gap: 20px; height: 40px;
  }
  .contacts svg { width: 28px; height: 28px; flex: none; }
  .accent-bar {
    position: absolute; left: 330px; right: 0; bottom: 0;
    height: 56px; background: var(--brand-cyan);
  }
  /* Back */
  .card--back {
    top: 622px;
    background: radial-gradient(ellipse at 45% 35%, var(--card-black-edge), var(--card-black) 75%);
  }
  .back-brand {
    position: absolute; inset: 0;
    display: flex; align-items: center; justify-content: center; gap: 22px;
  }
  .back-brand__dot {
    width: 86px; height: 86px; border-radius: 50%;
    border: 5px solid var(--emboss);
  }
  .back-brand__name {
    font-family: "Oswald", sans-serif; font-weight: 500;
    font-size: 64px; letter-spacing: 4px; text-transform: uppercase;
    color: var(--emboss);
  }
</style>
</head>
<body>
<main class="sheet">
  <section class="card card--front" aria-label="Business card front">
    <div class="brand">
      <span class="brand__dot"></span>
      <span class="brand__name">Bright Fern Realty</span>
    </div>
    <h1 class="holder">Maren Holt</h1>
    <ul class="contacts">
      <li>
        <svg viewBox="0 0 24 24" aria-hidden="true"><rect x="7" y="2" width="10" height="20" rx="2" fill="none" stroke="#1fb3ec" stroke-width="2"/><line x1="10" y1="18" x2="14" y2="18" stroke="#1fb3ec" stroke-width="2"/></svg>
        <span>0487 316 252</span>
      </li>
      <li>
        <svg viewBox="0 0 24 24" aria-hidden="true"><g fill="none" stroke="#1fb3ec" stroke-width="1.8"><circle cx="12" cy="12" r="9"/><ellipse cx="12" cy="12" rx="4" ry="9"/><line x1="3" y1="12" x2="21" y2="12"/></g></svg>
        <span>brightfernrealty.com.au</span>
      </li>
      <li>
        <svg viewBox="0 0 24 24" aria-hidden="true"><rect x="2" y="5" width="20" height="14" fill="#1fb3ec"/><polyline points="2,5 12,13 22,5" fill="none" stroke="#fff" stroke-width="1.8"/></svg>
        <span>hello@brightfernrealty.com.au</span>
      </li>
    </ul>
    <div class="accent-bar"></div>
  </section>

  <section class="card card--back" aria-label="Business card back">
    <div class="back-brand">
      <span class="back-brand__dot"></span>
      <span class="back-brand__name">Bright Fern Realty</span>
    </div>
  </section>
</main>
</body>
</html>
```